Design of a Flyer for my Lending team, depicts me at the top - leading the team

Need to design a Team flyer to be given to business partners and customers. The Velasko Team - Home Loan group is a team within Brightwell Home Loans. The brightwell home loans brand could be small than my brand. The purpose is to brand myself and my team in the marketplace while depicting a transaparent mortgage process.
See sample flyers. The flyer should be color and web and social media friendly as i will be posting on social media and HTML emails

Target Market(s)

Business to business and business to client

Industry/Entity Type

Mortgage Lender

Font styles to use
Serif
Sans Serif

Colors

Designer to choose colors to be used in the design.

Requirements
Must have
• My team Logo powered by Brightwell HOme loans
Nice to have
• Every team member picture and bio

```html
<!DOCTYPE html>
<html lang="en">
<head>
<meta charset="utf-8">
<title>The Velasko Team - Home Loan Group Flyer</title>
<link href="https://fonts.googleapis.com/css2?family=Lato:wght@400;700&family=Roboto+Condensed:wght@700&display=swap" rel="stylesheet">
<style>
:root{
  --stage:#6d6f6e;
  --paper:#ffffff;
  --blue:#0a6bbf;
  --blue-dark:#0b5aa3;
  --ink:#1d1d1d;
  --footer:#8a8a8a;
  --logo-gray:#6e6e70;
}
*{margin:0;padding:0;box-sizing:border-box}
html,body{width:1200px;height:1200px;overflow:hidden;background:var(--stage)}
body{font-family:'Lato',sans-serif;color:var(--ink);position:relative}
.flyer{position:absolute;left:193px;top:30px;width:813px;height:1140px;background:var(--paper);overflow:hidden}
.abs{position:absolute}
.icons{position:absolute;width:0;height:0}

.team-mark{left:146px;top:34px;width:44px;height:44px;background:var(--logo-gray)}
.team-name{left:40px;top:84px;width:260px;text-align:center;font-family:'Lato',sans-serif;font-weight:700;color:var(--blue);font-size:24px;line-height:26px;letter-spacing:.2px}
.team-name .sub{display:block;font-size:14px;letter-spacing:3px;line-height:18px}
.powered{left:648px;top:52px;font-size:16px;font-weight:700;color:#222}
.partner-mark{left:648px;top:78px;display:flex;align-items:center;gap:6px}
.partner-mark .sq{width:22px;height:22px;background:var(--blue-dark)}
.partner-mark .name{font-family:'Lato',sans-serif;font-weight:700;color:var(--blue-dark);font-size:12px;line-height:13px;letter-spacing:.5px}

.hero{left:0;top:138px;width:813px;height:358px;
  background:
   radial-gradient(ellipse at 75% 20%,#ffb43a 0%,rgba(255,150,40,.7) 25%,rgba(255,120,30,0) 55%),
   radial-gradient(ellipse at 20% 30%,#e88a2a 0%,rgba(200,110,30,.5) 35%,rgba(0,0,0,0) 65%),
   linear-gradient(180deg,#c77a2a 0%,#8d6a2a 45%,#4d7a2e 75%,#3f6b26 100%)}

.rule-thick{left:0;top:501px;width:813px;height:5px;background:var(--blue)}
.rule-thin{left:0;top:508px;width:813px;height:1.5px;background:var(--blue)}

.photo{border:2px solid var(--blue);background:linear-gradient(160deg,#e4e4e4,#9a9a9a)}
.photo.dark{background:linear-gradient(160deg,#3a3a3a,#111)}
.band .photo{border:none;background:linear-gradient(160deg,#d8d8d8,#8c8c8c)}

.name{font-family:'Roboto Condensed',sans-serif;font-weight:700;color:var(--blue);font-size:20px;line-height:22px;text-transform:uppercase}
.title{font-size:13px;font-weight:700;margin-top:6px}
.contact{font-size:11.5px;line-height:16px;margin-top:6px}
.contact div{display:flex;align-items:center;gap:6px;white-space:nowrap}
.contact svg{width:9px;height:9px;flex:none;fill:#666}
.contact b{font-weight:700}
.bio{font-size:11.6px;line-height:14.3px;text-align:justify}

.band{left:0;top:676px;width:813px;height:171px;background:var(--blue)}
.band .name,.band .contact,.band .bio{color:#fff}
.band .contact svg{fill:#fff}
.band .contact{margin-top:2px;line-height:15px}
.band .bio{margin-top:3px;font-size:11px;line-height:13.2px;letter-spacing:-.15px}

.rule-bottom{left:0;top:1004px;width:813px;height:4px;background:var(--blue)}
.footer{left:0;top:1010px;width:813px;height:130px;background:var(--footer)}
.legal{left:34px;top:1030px;width:746px;font-size:9.4px;line-height:12.6px;color:#fff}
</style>
</head>
<body>
<svg class="icons" aria-hidden="true">
  <symbol id="i-phone" viewBox="0 0 10 10"><path d="M2 .5l1.6 2.3-.9.9c.5 1.2 1.4 2.1 2.6 2.6l.9-.9L8.5 7 7.6 9C4 8.6 1.4 6 1 2.4z"/></symbol>
  <symbol id="i-fax" viewBox="0 0 10 10"><path d="M2.5 0h5v3h-5zM0 3.5h10V8H8v2H2V8H0zM3 6.5v2.5h4V6.5z"/></symbol>
  <symbol id="i-mail" viewBox="0 0 10 10"><path d="M0 2h10v6H0zM.8 2.6L5 5.6l4.2-3z" fill-rule="evenodd"/></symbol>
  <symbol id="i-pin" viewBox="0 0 10 10"><path d="M5 0a3.5 3.5 0 0 1 3.5 3.5C8.5 6 5 10 5 10S1.5 6 1.5 3.5A3.5 3.5 0 0 1 5 0zm0 2a1.5 1.5 0 1 0 0 3 1.5 1.5 0 0 0 0-3z"/></symbol>
</svg>

<main class="flyer">
  <header>
    <div class="abs team-mark"></div>
    <div class="abs team-name">THE VELASKO TEAM<span class="sub">HOME LOAN GROUP</span></div>
    <div class="abs powered">Powered by</div>
    <div class="abs partner-mark"><span class="sq"></span><span class="name">BRIGHTWELL<br>HOME LOANS</span></div>
  </header>

  <div class="abs hero" role="img" aria-label="Photo: two hands holding a small wooden house and a glass jar of coins against a warm sunset bokeh background"></div>
  <div class="abs rule-thick"></div>
  <div class="abs rule-thin"></div>

  <section class="lead">
    <div class="abs photo" style="left:36px;top:538px;width:101px;height:122px" role="img" aria-label="Portrait photo of Marco Velasko"></div>
    <div class="abs" style="left:148px;top:541px;width:238px">
      <div class="name">Marco Velasko</div>
      <div class="title">Producing Branch Manager</div>
      <div class="contact">
        <div><svg><use href="#i-phone"/></svg><span><b>(407) 555-0150</b> (Office)</span></div>
        <div><svg><use href="#i-fax"/></svg><span><b>(855) 555-0182</b> (Fax)</span></div>
        <div><svg><use href="#i-mail"/></svg><span>Marco.Velasko@brightwellhomeloans.com</span></div>
        <div><svg><use href="#i-pin"/></svg><span>Brightwell Home Loans, Inc – NMLS 40718</span></div>
      </div>
    </div>
    <p class="abs bio" style="left:393px;top:546px;width:359px">I have over 15 years of experience in Mortgage Planning. I rank in the top 1% of loan originators in the country. I pride myself on making the home buying process as smooth as possible. I will guide you through the mortgage process and look forward to helping you with your transaction. My team has been awarded with the Circle of Excellence award and CEO Club for being in the top 5 teams in the country having helped over 700+ families achieve the dream of home ownership between the years 2016 and 2017 and counting.</p>
  </section>

  <section class="abs band">
    <div class="abs photo" style="left:41px;top:18px;width:102px;height:123px" role="img" aria-label="Portrait photo of Rafael Montero"></div>
    <div class="abs" style="left:155px;top:13px;width:232px">
      <div class="name">Rafael Montero</div>
      <div class="contact">
        <div><svg><use href="#i-phone"/></svg><span><b>(407) 555-0172</b> &nbsp;&nbsp;&nbsp;(Direct/Text)</span></div>
        <div><svg><use href="#i-mail"/></svg><span>Rafael.Montero@brightwellhomeloans.com</span></div>
        <div><svg><use href="#i-pin"/></svg><span>Loan Partner I - NMLS ID 2730518</span></div>
      </div>
      <p class="bio">I am able to help customers with pre-qualifications and pre-approvals and keep the applicants and real estate agents informed during the application process.</p>
    </div>
    <div class="abs photo" style="left:413px;top:18px;width:101px;height:123px" role="img" aria-label="Portrait photo of Luis Carvalho"></div>
    <div class="abs" style="left:529px;top:13px;width:262px">
      <div class="name">Luis Carvalho</div>
      <div class="contact">
        <div><svg><use href="#i-phone"/></svg><span><b>(407) 555-0194</b> (Direct/Text)</span></div>
        <div><svg><use href="#i-mail"/></svg><span>Luis.Carvalho@brightwellhomeloans.com</span></div>
        <div><svg><use href="#i-pin"/></svg><span>Loan Processor – NMLS ID: 2815094</span></div>
      </div>
      <p class="bio">I verify loan documents including income, credit, appraisal and title insurance, preparing the loan application for submittal to underwriting. I review file documentation and make sure all items needed to ensure a smooth mortgage transaction are requested.</p>
    </div>
  </section>

  <section class="closer">
    <div class="abs photo dark" style="left:40px;top:866px;width:103px;height:124px" role="img" aria-label="Portrait photo of Helena Voss"></div>
    <div class="abs" style="left:168px;top:864px;width:612px">
      <div class="name">Helena Voss</div>
      <div class="contact" style="margin-top:3px">
        <div><svg><use href="#i-phone"/></svg><span><b>(631) 555-0151</b> (Direct/Text)</span></div>
        <div><svg><use href="#i-mail"/></svg><span>Helena.Voss@brightwellhomeloans.com</span></div>
        <div><svg><use href="#i-pin"/></svg><span>Closing Coordinator/Team Leader – NMLS 2904417</span></div>
      </div>
      <p class="bio" style="margin-top:3px">I guide our clients with any conditions or stipulations set by underwriting post loan conditional approval. I make sure all the transaction deadlines are met and help with preparing the loan for closing. I have over 20 years of experience with mortgage operations. I am committed to making sure all transactions close on time.</p>
    </div>
  </section>

  <div class="abs rule-bottom"></div>
  <footer class="abs footer"></footer>
  <p class="abs legal">Brightwell Home Loans, Inc. and any above mentioned companies are not affiliated.<br>
  Brightwell Home Loans, Inc., 800 Meadow Crest Dr, Plano, TX 75023 NMLS ID #40718 (http://www.lenderlookup-example.org/company/40718).<br>
  1-800-555-0142. Copyright © 2018.<br>
  All Rights Reserved. This is not an offer to enter into an agreement. Not all customers will qualify. Information, rates, and programs are subject to change without prior notice. All products are subject to credit and property approval. Not all products are available in all states or for all dollar amounts. If you are refinancing your existing loan, your total finance charges may be higher over the life of the loan. Other restrictions and limitations apply.</p>
</main>
</body>
</html>
```